Generic Label Design for Kids Craft Kits

I'm starting a new online / retail business that will package different craft materials and instructions into craft projects for kids from ages 2-12. I need a label for the front of the packages that looks professional. Although I'm interested in a very professional design (the kits will not be sold at a low cost) I'm also aiming for a 'natural' / crafty look to my packaging. The packaging will be hand-made with Kraft boxes / bags as the basic material. I will be adding hand-made embellishments to make the packaging look attractive (ex: a paper or crochet flower will be used to seal the packaging and hand-made twine ropes will be used as the handle). On the back of the package, I will be using a custom-made rubber stamp to imprint my Logo and Website address. I've included some pictures of packaging material that I really liked
Updates

       Please see updated brief and new deadline, this should make the project much clearer and easier.

Target Market(s)

End user = kids but buyer = parents

Industry/Entity Type

Business

Requirements
Must have

• The label design should include:
- A place for my logo at the top (it is a simple logo with the text: The Maple Makery in Google Fonts type Dancing Script. There is a small flower as the dot of the i in Makery)
- You can use these colors: #eaeac5, #e5b7b7, #669899, #947057, #8cc1ba, #fbfaf3 or any other similar / complementary colors
- a placeholder for me to add in (through photoshop) a digital image of the actual craft that is included in the package
- a place where I can put a small description of the activity or point out some cool features of the project
- a place where I can indicate the age suitability of the product
- a place where I can detail a short description of the activity,what is included in the kit

Other requirements:
- my online store is similar to this one in design so you can visit this for inspiration on look and feel: http://bramble-muffin-hollow.shopwren.example/
- the files that you provide should allow me to resize the label if I need to change the dimensions of my packaging (vector preferred)
- the look and feel should be attractive for children but still professional and sticking to the look and feel for my online store

```html
<!DOCTYPE html>
<html lang="en">
<head>
<meta charset="utf-8">
<title>The Maple Makery — Craft Kit Label</title>
<link rel="stylesheet" href="https://fonts.googleapis.com/css2?family=Dancing+Script:wght@600&family=Libre+Baskerville&display=swap">
<style>
  :root {
    --page: #ffffff;
    --strip-light: #cfe6e8;
    --strip-mid: #b6d6da;
    --strip-deep: #a4c9cc;
    --oval: #fbfaf0;
    --oval-edge: #f2f1df;
    --teal: #669899;
    --teal-soft: #8cc1ba;
    --frame: #eaddcf;
    --frame-inner: #f6f0e6;
    --ink: #7d7466;
  }
  * { margin: 0; padding: 0; box-sizing: border-box; }
  html, body { width: 857px; height: 1200px; overflow: hidden; background: var(--page); }
  .label { position: relative; width: 857px; height: 1200px; background: var(--page); }

  .pattern-strip {
    position: absolute; left: 271px; top: 0; width: 315px; height: 1200px;
    background: linear-gradient(180deg, var(--strip-light) 0%, var(--strip-mid) 35%, var(--strip-light) 60%, var(--strip-deep) 100%);
  }

  .info-oval {
    position: absolute; left: 71px; top: 386px; width: 729px; height: 328px;
    border-radius: 50%;
    background: radial-gradient(ellipse at center, var(--oval) 60%, var(--oval-edge) 100%);
    opacity: 0.96;
  }

  .brand-name {
    position: absolute; left: 0; width: 857px; top: 440px;
    text-align: center;
    font-family: "Dancing Script", cursive;
    font-weight: 600; font-size: 44px;
    color: var(--teal);
  }

  .photo-frame { position: absolute; left: 234px; top: 514px; width: 166px; height: 129px; }

  .product-block { position: absolute; left: 443px; top: 522px; width: 190px; }
  .product-title {
    font-family: "Libre Baskerville", serif;
    font-size: 13px; letter-spacing: 1px; color: var(--ink);
    margin-bottom: 6px;
  }
  .product-description {
    font-family: "Libre Baskerville", serif;
    font-size: 9.5px; line-height: 1.45; color: var(--ink);
  }

  .age-badge {
    position: absolute; left: 448px; top: 648px; width: 46px; height: 46px;
    border-radius: 50%; background: var(--teal);
    display: flex; align-items: center; justify-content: center; text-align: center;
    font-family: "Libre Baskerville", serif; font-size: 8px; line-height: 1.2;
    color: var(--oval);
  }
</style>
</head>
<body>
  <main class="label">
    <div class="pattern-strip" role="img" aria-label="Vertical band of soft blue, green and brown polka dots on a pale blue textured ground"></div>
    <div class="info-oval"></div>

    <h1 class="brand-name">The Maple Makery</h1>

    <svg class="photo-frame" viewBox="0 0 166 129" aria-label="Placeholder for a photo of the craft">
      <rect x="2" y="2" width="162" height="125" fill="var(--frame)" stroke="var(--frame)" stroke-width="4" stroke-dasharray="4 4" stroke-linecap="round"/>
      <rect x="16" y="16" width="134" height="97" fill="var(--frame-inner)"/>
      <rect x="24" y="24" width="118" height="81" fill="none" stroke="var(--frame)" stroke-width="2"/>
    </svg>

    <section class="product-block">
      <h2 class="product-title">PRODUCT TITLE</h2>
      <p class="product-description">Here you can share a short note about the activity or point out some fun features of the project.</p>
    </section>

    <div class="age-badge">Ages<br>4-8</div>
  </main>
</body>
</html>
```